Create a Shopify weblayout for Haverlow Fashion Boutique

I would like a new website layout for my online fashion boutique www.haverlow-shop.example. My new online boutique is inspired by the 2 English writers of the 19th century. These books come from old English literature. Haverlow is a fictitious place withing these inspiring love stories. My boutique idea is inspired by old English landscape, unprecedented magic and influenced by bonds between improbable characters. My boutique is for woman initially, but I would like to add male products sometime in the future, hence the logo should be gender neutral.

I have started with a logo which I deciding upon these days. However, the professional website layout that I am looking for would be inspired by a creative visual from the above descriptions.

I do like white/black color scheme, but I would also like the layout to incorporate an additional color plus an additional design element. I was thinking of floral inspirations, like roses or green wine leaves, perhaps. I would like something with a mix of modern, magic, and eclectic. Thank you all in advance for your igniting ideas.

Project Deadline Extended Reason: Project extended due to holiday season. We are working on submitting feedback regarding our desired layout. Added Thursday, November 24, 2016

Target Market(s)

Online boutique for women and man clothing.

Industry/Entity Type

Fashion

Coding

Coded - Design and coding required

Number of Pages Required

4 page

Font styles to use
Other font styles liked:
• readable, but elegant and artsy

Requirements
Must have
• Elegant, artsy and legible. Embrace the logo (vector files will be uploaded shortly)
• Files must support use with Shopify. More boutique style less commercial. Simple details are nice. I like the efficiency of the commercial sites. Must have a mobile version. EXAMPLE: http://www.mabelsonwestcedar.example/ THIS IS A BEAUTIFUL SITE. in place of the yellow line it would be nice to have a vine maybe?
• Although i am stern on this, i don't mean this with any disrespect ever but please, don't call me or email me on my personal email. If we need to connect, we can do so after i pick a design. Thank you.
Nice to have
• It would be nice if the tree of the logo would be incorporate somewhere in the website. We are very much interested in little details. Please inspire us.

```html
<!DOCTYPE html>
<html lang="en">
<head>
<meta charset="utf-8">
<title>Haverlow Fashion Boutique</title>
<link href="https://fonts.googleapis.com/css2?family=Playfair+Display:wght@400&family=Poppins:wght@300;400;500&display=swap" rel="stylesheet">
<style>
:root{
  --ink:#222831;
  --muted:#8a8f96;
  --navy:#1f2c3b;
  --navy-deep:#1a2533;
  --line:#e6e7ea;
  --card:#f2f3f6;
  --star:#f2a33a;
  --white:#ffffff;
}
*{box-sizing:border-box;margin:0;padding:0}
html,body{width:798px;height:1200px;overflow:hidden;background:var(--white)}
body{position:relative;font-family:'Poppins',sans-serif;color:var(--ink);font-size:9px}
.serif{font-family:'Playfair Display',serif;font-weight:400}
a{color:inherit;text-decoration:none}

.site-nav{position:absolute;top:0;left:0;width:798px;height:49px}
.site-nav a{position:absolute;top:20px;font-size:9.5px}
.site-nav .active{color:var(--muted)}
.brand{position:absolute;left:356px;top:22px;font-size:16px;letter-spacing:.5px;display:flex;align-items:center;gap:5px}
.brand .mark{width:6px;height:6px;background:var(--ink)}

.hero{position:absolute;left:59px;top:49px;width:680px;height:321px;background:linear-gradient(120deg,#2d3a4c 0%,#5a6f86 35%,#c8a27e 60%,#48b9c0 85%,#2a3340 100%)}
.hero-caption{position:absolute;left:42px;top:250px;width:159px;height:120px;background:var(--navy);color:var(--white);padding:20px 18px}
.hero-caption h1{font-size:12.5px;margin-bottom:10px}
.hero-caption p{font-size:7.8px;line-height:13px;font-weight:300}
.hero-caption .cta{position:absolute;left:88px;top:100px;font-size:6.8px;font-weight:500;display:flex;align-items:center;gap:3px}

.ornament{position:absolute;width:40px;height:8px;left:379px;background:#d9dbe0;border-radius:4px}
.section-title{position:absolute;width:798px;text-align:center;font-size:15px}

.product{position:absolute;top:444px;width:166px;height:201px;background:var(--card)}
.product .photo{position:absolute;left:18px;top:22px;width:130px;height:118px;border-radius:6px}
.product .price{position:absolute;left:10px;top:168px;font-size:8.5px}
.product .name{position:absolute;left:10px;top:180px;font-size:8.5px;font-weight:500;color:#444}
.product .count{position:absolute;right:10px;top:170px;font-size:6.5px}
.product .stars{position:absolute;right:10px;top:181px;font-size:7px;letter-spacing:1px;color:var(--star)}
.product .stars b{color:var(--ink);font-weight:400}

.btn{position:absolute;height:26px;border:1px solid var(--line);background:var(--white);font-size:8.5px;display:flex;align-items:center;justify-content:center}

.post{position:absolute;top:761px;width:211px;height:217px;background:var(--white);box-shadow:0 1px 4px rgba(0,0,0,.12)}
.post .photo{height:113px}
.post .tag{position:absolute;left:18px;top:133px;background:var(--navy);color:var(--white);font-size:6px;font-weight:500;padding:2px 6px}
.post h3{position:absolute;left:18px;top:149px;font-size:11px}
.post .meta{position:absolute;left:18px;top:169px;font-size:6.8px;color:#555;display:flex;gap:12px;align-items:center}
.post .meta span{display:flex;align-items:center;gap:3px}
.post .more{position:absolute;left:17px;top:196px;font-size:6.8px;display:flex;gap:4px;align-items:center}

.site-footer{position:absolute;left:0;top:1042px;width:798px;height:128px;background:var(--navy)}
.site-footer h4{position:absolute;top:30px;color:var(--white);font-size:11px;padding-bottom:3px;border-bottom:1px solid #7d8794}
.site-footer ul{position:absolute;top:60px;list-style:none;color:var(--white);font-size:8px;line-height:15px}
.subscribe{position:absolute;left:59px;top:62px;display:flex}
.subscribe input{width:137px;height:25px;border:none;padding:0 10px;font-family:'Poppins',sans-serif;font-size:6.5px;color:var(--muted)}
.subscribe button{width:26px;height:25px;background:var(--navy-deep);border:none;color:var(--white);display:flex;align-items:center;justify-content:center}

.bottom-bar{position:absolute;left:0;top:1170px;width:798px;height:30px;display:flex;align-items:center;justify-content:space-between;padding:0 59px;font-size:8.5px}
.payments{display:flex;gap:5px}
.payments span{width:21px;height:12px;border-radius:2px;background:#d6d9de}
</style>
</head>
<body>

<header class="site-nav">
  <a class="active" style="left:64px">Home</a>
  <a style="left:117px">The Team</a>
  <a style="left:187px">Designer Lines</a>
  <div class="brand serif"><span class="mark"></span>Haverlow</div>
  <a style="left:537px">Contact us</a>
  <a style="left:612px">Login</a>
  <a style="left:662px">Register</a>
  <svg style="position:absolute;left:718px;top:21px" width="14" height="10" viewBox="0 0 14 10" fill="none" stroke="#222831" stroke-width="1"><path d="M1 1h2l1.5 5h5l1.5-3.5H4"/><circle cx="5" cy="8.5" r=".8"/><circle cx="9" cy="8.5" r=".8"/><path d="M11.5 4l1 1 1-1"/></svg>
</header>

<div class="hero" role="img" aria-label="Photo of a smiling couple browsing clothes on a shop rail"></div>
<div class="hero-caption">
  <h1 class="serif">Haverlow Fashion</h1>
  <p>Lorem aenean vulputate eleifend tellus aenean leo ligula porttitor eu dolor sit.</p>
  <a class="cta">SHOP NOW <svg width="8" height="6" viewBox="0 0 8 6" fill="none" stroke="#fff"><path d="M0 3h7M5 1l2 2-2 2"/></svg></a>
</div>

<div class="ornament" style="top:402px" role="img" aria-label="Small floral flourish"></div>
<h2 class="section-title serif" style="top:411px">Haverlow’s Collection</h2>

<div class="product" style="left:61px"><div class="photo" role="img" aria-label="Purple fedora hat" style="background:radial-gradient(#7b62d6,#f2f3f6 70%)"></div><div class="price">$16.90</div><div class="name">Product name here</div><div class="count">24</div><div class="stars"><b>★</b>★★★★</div></div>
<div class="product" style="left:230px"><div class="photo" role="img" aria-label="Blue denim shirt" style="background:radial-gradient(#2f4f8f,#f2f3f6 70%)"></div><div class="price">$25.45</div><div class="name">Product name here</div><div class="count">24</div><div class="stars"><b>★</b>★★★★</div></div>
<div class="product" style="left:400px"><div class="photo" role="img" aria-label="Grey canvas sneaker" style="background:radial-gradient(#9d9a92,#f2f3f6 65%)"></div><div class="price">$12.00</div><div class="name">Product name here</div><div class="count">24</div><div class="stars"><b>★</b>★★★★</div></div>
<div class="product" style="left:570px"><div class="photo" role="img" aria-label="Pair of white loafers" style="background:radial-gradient(#ffffff,#e4e6ea 70%)"></div><div class="price">$54.75</div><div class="name">Product name here</div><div class="count">24</div><div class="stars"><b>★</b>★★★★</div></div>

<a class="btn" style="left:356px;top:664px;width:86px">View full boutique</a>

<div class="ornament" style="top:719px" role="img" aria-label="Small floral flourish"></div>
<h2 class="section-title serif" style="top:728px">Blogs</h2>

<article class="post" style="left:59px">
  <div class="photo" role="img" aria-label="Two women holding shopping bags" style="background:linear-gradient(120deg,#c7b26a,#e8d24a 40%,#8cc6d8 70%,#e08a3b)"></div>
  <span class="tag">FASHION</span><h3 class="serif">Lorem ipsum dolor dummy.</h3>
  <div class="meta"><span>● By: admin</span><span>▢ Posted on: 20.July.2016</span></div>
  <a class="more">READ BLOG <svg width="8" height="6" viewBox="0 0 8 6" fill="none" stroke="#222831"><path d="M0 3h7M5 1l2 2-2 2"/></svg></a>
</article>
<article class="post" style="left:294px">
  <div class="photo" role="img" aria-label="Woman reading a price tag in a clothing store" style="background:linear-gradient(120deg,#5d4a3e,#a7896f 40%,#cfd3d8 70%,#3d4d66)"></div>
  <span class="tag">WOMEN</span><h3 class="serif">Lorem ipsum dolor dummy.</h3>
  <div class="meta"><span>● By: admin</span><span>▢ Posted on: 20.July.2016</span></div>
  <a class="more">READ BLOG <svg width="8" height="6" viewBox="0 0 8 6" fill="none" stroke="#222831"><path d="M0 3h7M5 1l2 2-2 2"/></svg></a>
</article>
<article class="post" style="left:528px">
  <div class="photo" role="img" aria-label="Couple walking through a shopping mall with bags" style="background:linear-gradient(120deg,#9bb3c9,#e6e8ea 40%,#5c8bbf 70%,#c9a86a)"></div>
  <span class="tag">TRENDS</span><h3 class="serif">Lorem ipsum dolor dummy.</h3>
  <div class="meta"><span>● By: admin</span><span>▢ Posted on: 20.July.2016</span></div>
  <a class="more">READ BLOG <svg width="8" height="6" viewBox="0 0 8 6" fill="none" stroke="#222831"><path d="M0 3h7M5 1l2 2-2 2"/></svg></a>
</article>

<a class="btn" style="left:368px;top:998px;width:63px">More Blogs</a>

<footer class="site-footer">
  <h4 class="serif" style="left:59px">Subscribe</h4>
  <form class="subscribe"><input type="email" placeholder="Email address"><button type="button"><svg width="8" height="6" viewBox="0 0 8 6" fill="none" stroke="#fff"><path d="M0 3h7M5 1l2 2-2 2"/></svg></button></form>
  <h4 class="serif" style="left:288px">Navigation</h4>
  <ul style="left:288px"><li>Home</li><li>Search</li><li>About us</li></ul>
  <h4 class="serif" style="left:430px">Shop by collection</h4>
  <ul style="left:430px"><li>Business / Formal</li><li>Casual</li><li>Party</li></ul>
  <h4 class="serif" style="left:584px">Shop by category</h4>
  <ul style="left:584px"><li>Men</li><li>Women</li><li>All</li></ul>
</footer>

<div class="bottom-bar">
  <span>© Haverlow</span>
  <div class="payments"><span></span><span></span><span></span><span></span></div>
</div>

</body>
</html>
```